Stylish new business card needed!

Hello everyone! I am in need of a new business card design for an alarm company here in Hurricane WV. I have all fonts, color codes and logos provided for you use! We are a young company and like the style of a clean sleek looking business card. Would like it double sided, one side holding the logo and the other with your design!
Target Market(s)
The people that are looking for the newest tech for home automation and security
Industry/Entity Type
Alarm services; Home automation
Contact Information for Business Card
Name of person; position (Sales; Installer); Phone Number (555.418.7290); Employee cell Number; Website (www.GuardedByVemlo.example); Employee Email; Double sided
Look and feel
Each slider illustrates characteristics of the customer's brand and the style your logo design should communicate.

```html
<!DOCTYPE html>
<html lang="en">
<head>
<meta charset="utf-8">
<title>Vemlo Business Card</title>
<link href="https://fonts.googleapis.com/css2?family=Oswald:wght@300;400;500&family=Archivo+Black&display=swap" rel="stylesheet">
<style>
  :root {
    --stage: #e2e2e2;
    --ink: #000000;
    --paper: #ffffff;
    --divider: #e6e6e6;
    --orange: #ff914d;
    --grey: #999999;
    --text-grey: #666666;
  }
  * { margin: 0; padding: 0; box-sizing: border-box; }
  html, body { width: 1200px; height: 1200px; overflow: hidden; }
  body { background: var(--stage); position: relative; font-family: 'Oswald', sans-serif; }

  .card { position: absolute; left: 294px; width: 612px; height: 349px; overflow: hidden; }
  .card--front { top: 229px; background: var(--paper); }
  .card--back { top: 622px; background: var(--ink); }

  .front__brand-panel { position: absolute; left: 0; top: 0; width: 207px; height: 332px; background: var(--ink); }
  .front__divider { position: absolute; left: 207px; top: 0; width: 9px; height: 332px; background: var(--divider); }
  .front__band { position: absolute; left: 0; bottom: 0; width: 100%; height: 17px; background: var(--orange); }

  .vertical-brand { position: absolute; left: 103px; top: 108px; transform: translateX(-50%) rotate(90deg); transform-origin: center; display: flex; align-items: center; gap: 12px; }
  .vertical-brand__name { font-weight: 400; font-size: 64px; letter-spacing: 6px; color: var(--grey); line-height: 1; }
  .brand-dot { width: 18px; height: 18px; border-radius: 50%; background: var(--orange); flex: none; }

  .contact { position: absolute; left: 243px; top: 73px; color: var(--text-grey); }
  .contact__name { font-weight: 400; font-size: 25px; line-height: 1.2; }
  .contact__role { font-weight: 300; font-size: 19px; color: var(--orange); margin-top: 1px; }
  .contact__list { list-style: none; margin-top: 26px; font-weight: 300; font-size: 19px; line-height: 28.4px; }

  .back__band-grey { position: absolute; left: 0; bottom: 0; width: 207px; height: 16px; background: var(--grey); }
  .back__band-orange { position: absolute; left: 207px; bottom: 0; width: 405px; height: 16px; background: var(--orange); }
  .back__lockup { position: absolute; left: 0; right: 0; top: 95px; text-align: center; }
  .back__kicker { font-family: 'Archivo Black', sans-serif; font-size: 23px; letter-spacing: 1.5px; color: var(--orange); line-height: 1; }
  .back__brand { display: flex; justify-content: center; align-items: center; gap: 16px; margin-top: 12px; }
  .back__brand-name { font-weight: 400; font-size: 92px; letter-spacing: 4px; color: var(--grey); line-height: 1; }
  .back__brand .brand-dot { width: 26px; height: 26px; }
  .back__tagline { font-family: 'Archivo Black', sans-serif; font-size: 9.5px; letter-spacing: 0.6px; color: var(--orange); margin-top: 14px; }
</style>
</head>
<body>
  <section class="card card--front">
    <div class="front__brand-panel">
      <div class="vertical-brand">
        <span class="vertical-brand__name">VEMLO</span>
        <span class="brand-dot"></span>
      </div>
    </div>
    <div class="front__divider"></div>
    <div class="contact">
      <p class="contact__name">Name of Person</p>
      <p class="contact__role">Position (Sales; Installer)</p>
      <ul class="contact__list">
        <li>Phone: (555.418.7290)</li>
        <li>Employee Cell: (000000000)</li>
        <li>Website: www.GuardedByVemlo.example</li>
        <li>Employee Email: info@vemlo.example</li>
      </ul>
    </div>
    <div class="front__band"></div>
  </section>

  <section class="card card--back">
    <div class="back__lockup">
      <p class="back__kicker">GUARDED BY</p>
      <div class="back__brand">
        <span class="brand-dot"></span>
        <span class="back__brand-name">VEMLO</span>
      </div>
      <p class="back__tagline">AUTOMATION AND SECURITY SERVICES</p>
    </div>
    <div class="back__band-grey"></div>
    <div class="back__band-orange"></div>
  </section>
</body>
</html>
```